Award-winnning Estate Agent needs a premium version of their 'For Sale' board design

We need a premium option for our 'For Sale' board design. We have a standard board that is attached to this brief, but were are looking to have a premium design version that we will use when selling exclusive properties. Our company name is Harbour Lane Estates and the name for this is exclusive selection is: 'The Harbour Collection'. The design needs to work with our current brand, but have a distinctive PREMIUM feel to it. I have uploaded the barnd guidelines and also some of the exisisting logo variations. We do NOT need a new logo but feel free to play around with colours, fonts, sizes etc. for the sign.

Target Market(s)

Property buyers & house hunters

Industry/Entity Type

Real Estate - Residential Property

Font styles to use
Sans Serif

Requirements
Must have
• A premium fee, must be square design, must be easy to read when driving past the sign
Nice to have
• I'm open ot ideas

```html
<!DOCTYPE html>
<html lang="en">
<head>
<meta charset="utf-8">
<title>Harbour Lane Estates – For Sale Board</title>
<link rel="stylesheet" href="https://fonts.googleapis.com/css2?family=Arimo:wght@400;700&display=swap">
<style>
  :root {
    --sky: #38a9df;
    --navy: #2d378b;
    --board: #ffffff;
    --page: #fcfcfc;
  }
  html, body {
    margin: 0;
    padding: 0;
    width: 1200px;
    height: 1200px;
    overflow: hidden;
    background: var(--page);
  }
  .canvas {
    position: relative;
    width: 1200px;
    height: 1200px;
  }
  .sale-board {
    position: absolute;
    left: 364px;
    top: 364px;
    width: 472px;
    height: 472px;
    display: block;
  }
  .sale-board text { font-family: "Arimo", Arial, sans-serif; }
  .board-base { fill: var(--board); }
  .sky-panel { fill: var(--sky); }
  .navy-wedge { fill: var(--navy); }
  .headline { fill: #ffffff; font-weight: 700; font-size: 90px; }
  .collection-name { fill: var(--navy); font-weight: 700; font-size: 35px; }
  .phone { fill: var(--navy); font-weight: 700; font-size: 78px; }
  .web-band { fill: var(--sky); }
  .base-rule { fill: var(--navy); }
  .web-address { fill: #ffffff; font-weight: 400; font-size: 35px; }
</style>
</head>
<body>
<main class="canvas">
  <svg class="sale-board" viewBox="455 455 590 590" xmlns="http://www.w3.org/2000/svg" role="group" aria-label="Harbour Lane Estates for sale board">
    <rect class="board-base" x="455" y="455" width="590" height="590"/>
    <polygon class="sky-panel" points="455,455 1045,455 1045,490 455,780"/>
    <polygon class="navy-wedge" points="916,563 1045,500 1045,648"/>

    <text class="headline" x="476" y="552">FOR SALE</text>

    <text class="collection-name" x="1000" y="827" text-anchor="end">The Harbour Collection</text>

    <text class="phone" x="1000" y="920" text-anchor="end" textLength="503" lengthAdjust="spacingAndGlyphs">01632 960418</text>

    <rect class="web-band" x="455" y="948" width="590" height="86"/>
    <rect class="base-rule" x="455" y="1033" width="590" height="12"/>
    <text class="web-address" x="750" y="1002" text-anchor="middle">www.harbourlaneestates.co.uk</text>
  </svg>
</main>
</body>
</html>
```